Design for the A4 Letterhead, envelope and A4 Folder

Design have to be clean, professional, unique (eye catchy) and high end.
Colors: Yellow (Code: 803C), Darker Grey and Black or white (optional)
Logo can be in white or black

Letterhead:
Contain: 1. Korvanel Logo
2. Slogan "MADE WITH PRIDE"
3. Company information:
Korvanel Valves Pte. Ltd. (Singapore)
Registration no: 201947162K
Tel: (65) 6218 4906
Fax: (65) 6241 7089
Email: sales@korvanelvalves.example
Website: http://www.korvanelvalves.example
4. Logo watermark

Envelope:
Contain: 1. Korvanel Logo
3. website: http://www.korvanelvalves.example and email address:
sales@korvanelvalves.example
4. Logo watermark

Folder:
Contain: 1. Korvanel Logo
3. Company's information:
Tel: (65) 6218 4906
Fax: (65) 6241 7089
4. QR Code
5. Logo watermark
6. On the inside there is a space to insert business card. Contrast colors
between the inside and cover.

For the Folder design, please be informed that we would prefer to have the Korvanel logo on the left hand side of the cover page, rather than on the right hand side.And also if we could highlight the "Made with Pride" slogan with either the yellow box or black/grey box depending on the background color.For the Envelope design,it does not matter where the position of the logo is. But please also highlight the "Made with Pride" Slogan For the Letterhead design, the position of the logo must be on the left hand side and the slogan must be highlighted. In addition, please include the following company information (only for the letterhead design)Korvanel Valves Pte. Ltd. (Singapore)Registration no: 201947162KTel: (65) 6218 4906Fax: (65) 6241 7089Email: sales@korvanelvalves.exampleWebsite: http://www.korvanelvalves.example Added Wednesday, August 2, 2017

Target Market(s)

Business to Business, High End market

Industry/Entity Type

It Professional

Font styles to use
Serif

Requirements
Must have
• Design have to be clean, professional, unique (eye catchy) and high end.
Nice to have
• color contrast but still maintaining the professionalism and the seriousness
Should not have
• Messy look, futuristic look, too crowded

```html
<!DOCTYPE html>
<html lang="en">
<head>
<meta charset="utf-8">
<title>Korvanel Valves Letterhead</title>
<link rel="stylesheet" href="https://fonts.googleapis.com/css2?family=Noto+Serif:wght@400;700&family=Open+Sans:wght@400;700&display=swap">
<style>
  :root {
    --yellow: #f5e12a;
    --yellow-deep: #e9d30f;
    --black: #111111;
    --grey-dark: #3a3a3a;
    --paper: #ffffff;
    --stage: #ececec;
    --mark: #f2f2f2;
  }
  * { margin: 0; padding: 0; box-sizing: border-box; }
  html, body { width: 1200px; height: 784px; overflow: hidden; }
  body {
    background: var(--stage);
    display: flex;
    align-items: center;
    justify-content: center;
    font-family: "Open Sans", Arial, sans-serif;
  }
  .letterhead {
    position: relative;
    width: 523px;
    height: 740px;
    background: var(--paper);
    box-shadow: 0 2px 10px rgba(0,0,0,.12);
    overflow: hidden;
  }
  .logo-tab {
    position: absolute;
    left: 0; top: 0;
    width: 112px; height: 66px;
    background: var(--black);
    border-bottom-right-radius: 16px;
    display: flex;
    align-items: center;
    justify-content: center;
    gap: 6px;
  }
  .logo-tab .logo-dot {
    width: 14px; height: 14px;
    border: 2px solid #fff;
    border-radius: 50%;
  }
  .logo-tab .logo-name {
    color: #fff;
    font-family: "Noto Serif", Georgia, serif;
    font-weight: 700;
    font-size: 13px;
    letter-spacing: 1px;
  }
  .header-rule {
    position: absolute;
    left: 0; top: 0;
    width: 523px; height: 80px;
  }
  .header-info {
    position: absolute;
    right: 24px; top: 78px;
    text-align: right;
  }
  .slogan {
    font-family: "Noto Serif", Georgia, serif;
    font-weight: 700;
    font-size: 27px;
    letter-spacing: 1px;
    color: var(--yellow-deep);
    line-height: 1;
  }
  .company-name {
    margin-top: 6px;
    font-weight: 700;
    font-size: 9.5px;
    color: var(--black);
  }
  .contact-line {
    margin-top: 5px;
    font-size: 7px;
    color: var(--grey-dark);
    display: flex;
    justify-content: flex-end;
    gap: 8px;
  }
  .contact-line span::before {
    content: "";
    display: inline-block;
    width: 5px; height: 5px;
    margin-right: 3px;
    border-radius: 50%;
    background: var(--grey-dark);
    vertical-align: middle;
  }
  .watermark {
    position: absolute;
    left: 95px; top: 255px;
    width: 300px; height: 300px;
    border: 22px solid var(--mark);
    border-radius: 50%;
    display: flex;
    align-items: center;
    justify-content: center;
  }
  .watermark-name {
    font-family: "Noto Serif", Georgia, serif;
    font-weight: 700;
    font-size: 38px;
    letter-spacing: 3px;
    color: var(--mark);
  }
  .footer-rule {
    position: absolute;
    left: 0; bottom: 0;
    width: 523px; height: 44px;
  }
  .reg-no {
    position: absolute;
    right: 10px; bottom: 9px;
    color: #fff;
    font-weight: 700;
    font-size: 9px;
  }
</style>
</head>
<body>
  <main class="letterhead">
    <svg class="header-rule" viewBox="0 0 523 80" aria-hidden="true">
      <path d="M100 66 Q112 66 118 72 L523 72" fill="none" stroke="var(--yellow)" stroke-width="3"/>
      <path d="M112 70 L523 70" fill="none" stroke="var(--yellow-deep)" stroke-width="1"/>
    </svg>
    <div class="logo-tab">
      <span class="logo-dot"></span>
      <span class="logo-name">KORVANEL</span>
    </div>

    <header class="header-info">
      <p class="slogan">MADE WITH PRIDE</p>
      <p class="company-name">Korvanel Valves Pte. Ltd. (Singapore)</p>
      <p class="contact-line">
        <span>(65) 6218 4906</span>
        <span>(65) 6241 7089</span>
        <span>sales@korvanelvalves.example</span>
        <span>www.korvanelvalves.example</span>
      </p>
    </header>

    <div class="watermark" aria-hidden="true">
      <span class="watermark-name">KORVANEL</span>
    </div>

    <svg class="footer-rule" viewBox="0 0 523 44" aria-hidden="true">
      <path d="M0 38 L160 38 L168 30 L400 30" fill="none" stroke="var(--black)" stroke-width="5"/>
      <path d="M170 24 L400 24" fill="none" stroke="var(--yellow)" stroke-width="3"/>
      <path d="M0 44 L0 41 L400 41 L412 18 L523 18 L523 44 Z" fill="var(--black)"/>
      <path d="M0 41 L400 41" stroke="var(--grey-dark)" stroke-width="1"/>
    </svg>
    <p class="reg-no">Regd. No: 201947162K</p>
  </main>
</body>
</html>
```